Fernbrook Plots - Online-only garden installation company

Online-only garden installation company. Our demographic is middle aged / suburban women, and we anticipate Facebook driving traffic to this website, as well as referrals from garden centers. The website must be very simple in design and function.

All orders will be placed through the website, including size of garden (3 options), location in yard, payment, and scheduling of installation date.

The website should employ a 3 step process:

Step 1: Select garden size. Either an 4' X 4', 8' X 4', or 12' X 4'.

Step 2: Select a location. We would like to use google maps to look up a US address, then "drag and drop" one of the garden sizes from step 1 to the location the customer would like us to install the garden at their home.

Step 3: Pick an installation date and pay. Using an online calendar the customer will pick a date, and then pay for the installation via credit card.

The website will be linked to an email account, FernbrookPlots@mailvessel.com to inform us of orders placed.

Target Market(s)

Our demographic is middle aged / suburban women, and we anticipate Facebook driving traffic to this website, as well as referrals from garden centers.

Industry/Entity Type

It Company

Coding

Coded - Design and coding required

Number of Pages Required

4 page

Requirements
Must have
• Scheduling and payment options.

```html
<!DOCTYPE html>
<html lang="en">
<head>
<meta charset="utf-8">
<title>Fernbrook Plots – Garden Installation</title>
<link href="https://fonts.googleapis.com/css2?family=Arimo:wght@400;700&family=Bitter:wght@400;700&family=Open+Sans:wght@400&family=Raleway:wght@400&family=Tinos:wght@400&display=swap" rel="stylesheet">
<style>
:root{
  --orange:#e4532a;
  --orange-dark:#c93f17;
  --orange-text:#e0501f;
  --green:#3a8a3c;
  --green-deep:#2f7431;
  --ink:#222;
  --grey-line:#d8d8d8;
  --footer-a:#2c3a22;
  --footer-b:#3f4a2a;
  --white:#fff;
}
*{margin:0;padding:0;box-sizing:border-box}
html,body{width:1021px;height:1200px;overflow:hidden;background:var(--white)}
body{position:relative;font-family:"Arimo",sans-serif;color:var(--ink)}

.site-header{position:absolute;top:0;left:0;width:1021px;height:114px;background:var(--white);z-index:3;border-bottom:1px solid #e6e6e6}
.logo-tab{position:absolute;left:78px;top:0;width:156px;height:152px;z-index:4}
.logo-name{position:absolute;left:84px;top:72px;width:144px;text-align:center;font-family:"Bitter",serif;font-weight:700;font-size:17px;line-height:20px;color:var(--ink);z-index:5}
.logo-mark{position:absolute;left:146px;top:38px;width:20px;height:20px;background:var(--green);z-index:5}
.helpline{position:absolute;right:80px;top:24px;display:flex;align-items:center;gap:12px}
.helpline .note{font-size:10.5px;color:var(--orange-text)}
.helpline .number{font-size:19px;color:var(--ink)}
.main-nav{position:absolute;right:75px;top:75px;display:flex;font-family:"Bitter",serif;font-size:13px}
.main-nav a{color:var(--ink);text-decoration:none;padding:0 25px;border-left:1px solid #ddd;line-height:14px}
.main-nav a:first-child{border-left:none;color:var(--orange-text)}
.main-nav a:last-child{padding-right:0}

.hero{position:absolute;top:114px;left:0;width:1021px;height:397px;background:linear-gradient(90deg,#4f7f2e 0%,#7aa844 30%,#5d8d33 50%,#8db552 72%,#557f2c 100%)}
.hero .soil{position:absolute;left:20px;right:20px;bottom:30px;height:140px;background:linear-gradient(180deg,rgba(120,70,40,.0),rgba(130,70,35,.55))}
.hero-arrow{position:absolute;top:206px;width:22px;height:40px}
.hero-caption{position:absolute;left:200px;top:318px;width:624px;height:60px;background:rgba(40,40,40,.55);color:var(--white);font-family:"Raleway",sans-serif;font-size:26px;text-align:center;line-height:60px}

.sizes-title{position:absolute;top:548px;left:0;width:1021px;text-align:center;font-family:"Bitter",serif;font-weight:700;font-size:25px;color:var(--ink)}
.sizes-rule{position:absolute;top:589px;left:472px;width:77px;height:2px;background:var(--green-deep)}

.size-card{position:absolute;top:613px;width:280px;height:258px;border:1px solid var(--grey-line);background:var(--white)}
.size-card .bed{position:absolute;left:40px;top:22px;width:198px;height:160px;border-radius:6px;background:linear-gradient(180deg,#3f7d2c 0%,#5f9a3a 55%,#d6b47a 56%,#c9a164 100%)}
.size-card .blurb{position:absolute;left:29px;top:196px;font-size:13.5px;color:var(--ink)}
.size-bar{position:absolute;left:-1px;right:-1px;bottom:-1px;height:30px;background:var(--orange);display:flex;align-items:center;padding:0 8px 0 10px;color:var(--white)}
.size-bar .size{font-size:13.5px;flex:1}
.size-bar .price{background:var(--orange-dark);border-radius:3px;font-weight:700;font-size:13px;padding:4px 10px;margin-right:6px}
.size-bar .buy{background:var(--orange-dark);border-radius:3px;font-family:"Open Sans",sans-serif;font-size:11px;padding:5px 15px;display:flex;align-items:center;gap:6px}

.site-footer{position:absolute;top:934px;left:0;width:1021px;height:228px;border-radius:40px 40px 0 0;background:linear-gradient(90deg,var(--footer-a) 0%,#33401f 45%,#5a4a2c 75%,var(--footer-b) 100%);color:var(--white)}
.footer-col h3{font-family:"Tinos",serif;font-weight:400;font-size:15px;padding-bottom:8px;border-bottom:1px solid rgba(255,255,255,.15);margin-bottom:12px}
.about{position:absolute;left:70px;top:32px;width:215px}
.about p{font-size:11px;line-height:19px}
.contact{position:absolute;left:330px;top:32px;width:180px}
.contact .row{display:flex;align-items:center;gap:9px;font-family:"Open Sans",sans-serif;font-size:12px;margin-bottom:16px}
.social{display:flex;gap:6px}
.social span{width:25px;height:25px;background:#6b7f5a}
.newsletter{position:absolute;left:556px;top:32px;width:180px}
.newsletter p{font-family:"Open Sans",sans-serif;font-size:10.5px;line-height:15px;margin-bottom:10px}
.newsletter .field{width:168px;height:22px;background:var(--white);border-radius:3px;color:#333;font-family:"Open Sans",sans-serif;font-size:10px;line-height:22px;padding-left:6px;margin-bottom:13px}
.newsletter .subscribe{display:inline-block;background:var(--green);font-size:12px;padding:5px 13px;border-radius:2px}
.footer-name{position:absolute;left:770px;top:110px;width:170px;text-align:center;font-family:"Bitter",serif;font-weight:700;font-size:19px;color:rgba(255,255,255,.5)}
.footer-name::before{content:"";display:block;width:16px;height:16px;margin:0 auto 8px;background:rgba(255,255,255,.5)}

.legal-bar{position:absolute;top:1162px;left:0;width:1021px;height:38px;background:var(--green);color:var(--white);font-family:"Tinos",serif;font-size:12px}
.legal-bar .copy{position:absolute;left:71px;top:12px}
.legal-bar .accept{position:absolute;right:30px;top:9px;display:flex;align-items:center;gap:6px}
.legal-bar .accept em{font-style:normal;margin-right:9px}
.legal-bar .card{width:30px;height:19px;background:var(--white);border-radius:2px}
</style>
</head>
<body>

<header class="site-header">
  <div class="helpline">
    <span class="note">Need any help? Call Us Anytime</span>
    <svg width="26" height="26" viewBox="0 0 24 24" aria-hidden="true"><path fill="#3a8a3c" d="M6.6 10.8c1.4 2.8 3.8 5.1 6.6 6.6l2.2-2.2c.3-.3.7-.4 1-.2 1.1.4 2.3.6 3.6.6.6 0 1 .4 1 1V20c0 .6-.4 1-1 1C10.6 21 3 13.4 3 4c0-.6.4-1 1-1h3.5c.6 0 1 .4 1 1 0 1.3.2 2.5.6 3.6.1.3 0 .7-.2 1z"/></svg>
    <span class="number">123-456-7890</span>
  </div>
  <nav class="main-nav">
    <a href="#">HOME</a>
    <a href="#">How We Work</a>
    <a href="#">BASKET</a>
    <a href="#">CONTACT US</a>
  </nav>
</header>

<svg class="logo-tab" viewBox="0 0 156 152" aria-hidden="true"><path d="M0 0H156V114L78 152L0 114Z" fill="#fff"/></svg>
<span class="logo-mark"></span>
<div class="logo-name">FERNBROOK PLOTS</div>

<section class="hero" role="img" aria-label="Two women planting vegetables in raised wooden garden beds on a lawn">
  <div class="soil"></div>
  <svg class="hero-arrow" style="left:24px" viewBox="0 0 22 40" aria-hidden="true"><path d="M20 2L2 20l18 18" stroke="#fff" stroke-width="2" fill="none"/></svg>
  <svg class="hero-arrow" style="right:24px" viewBox="0 0 22 40" aria-hidden="true"><path d="M2 2l18 18L2 38" stroke="#fff" stroke-width="2" fill="none"/></svg>
  <div class="hero-caption">We Are Online-only Garden Installation Company</div>
</section>

<h2 class="sizes-title">Select Size Of The Garden</h2>
<div class="sizes-rule"></div>

<article class="size-card" style="left:68px">
  <div class="bed" role="img" aria-label="Small cedar raised bed filled with vegetable plants"></div>
  <p class="blurb">Lorem Ispum is the Dummy Text</p>
  <div class="size-bar"><span class="size">Size : 4' X 4'</span><span class="price">$175.00</span><span class="buy"><svg width="12" height="10" viewBox="0 0 12 10"><path d="M0 0h2l1 6h7l1.5-4.5H3" stroke="#fff" fill="none"/><circle cx="4" cy="8.8" r="1" fill="#fff"/><circle cx="9" cy="8.8" r="1" fill="#fff"/></svg>Buy Now</span></div>
</article>

<article class="size-card" style="left:370px">
  <div class="bed" role="img" aria-label="Medium cedar raised bed filled with vegetable plants"></div>
  <div class="size-bar"><span class="size">Size : 8' X 4'</span><span class="price">$275.00</span><span class="buy"><svg width="12" height="10" viewBox="0 0 12 10"><path d="M0 0h2l1 6h7l1.5-4.5H3" stroke="#fff" fill="none"/><circle cx="4" cy="8.8" r="1" fill="#fff"/><circle cx="9" cy="8.8" r="1" fill="#fff"/></svg>Buy Now</span></div>
</article>

<article class="size-card" style="left:673px">
  <div class="bed" style="left:12px;width:256px" role="img" aria-label="Large cedar raised bed filled with vegetable plants"></div>
  <div class="size-bar"><span class="size">Size : 12' X 4'</span><span class="price">$375.00</span><span class="buy"><svg width="12" height="10" viewBox="0 0 12 10"><path d="M0 0h2l1 6h7l1.5-4.5H3" stroke="#fff" fill="none"/><circle cx="4" cy="8.8" r="1" fill="#fff"/><circle cx="9" cy="8.8" r="1" fill="#fff"/></svg>Buy Now</span></div>
</article>

<footer class="site-footer" role="img" aria-label="Dark background of freshly pulled carrots">
  <div class="footer-col about">
    <h3>About Us</h3>
    <p>Lorem ipsum dolor rrsit amet, consectetuer adipiscing efdflit, sed diarm nonummy nibh euismod tincidunt ut laoreet dolona aliquam erat volutpat. Ut wisi enim ad mim ventirrm, quis nostrud exerci tation ullamcer surscipit lo Duis autem vel eum iriure drelor iendrerit in vulputate velit esse molestie conquat, vel illum dolore eu feugiat nulla.</p>
  </div>
  <div class="footer-col contact">
    <h3>Contact Info</h3>
    <div class="row"><svg width="11" height="11" viewBox="0 0 24 24"><path fill="#5fae4f" d="M6.6 10.8c1.4 2.8 3.8 5.1 6.6 6.6l2.2-2.2c.3-.3.7-.4 1-.2 1.1.4 2.3.6 3.6.6.6 0 1 .4 1 1V20c0 .6-.4 1-1 1C10.6 21 3 13.4 3 4c0-.6.4-1 1-1h3.5c.6 0 1 .4 1 1 0 1.3.2 2.5.6 3.6.1.3 0 .7-.2 1z"/></svg>123 - 456 - 7890</div>
    <div class="row"><svg width="12" height="9" viewBox="0 0 12 9"><rect width="12" height="9" fill="#5fae4f"/><path d="M0 0l6 5 6-5" stroke="#2c3a22" fill="none"/></svg>hello@fernbrookplots.com</div>
    <h3 style="margin-top:22px">Social Media</h3>
    <div class="social"><span></span><span></span><span></span><span></span></div>
  </div>
  <div class="footer-col newsletter">
    <h3>Newsletter Signup</h3>
    <p>Get latest updates by entering your email address</p>
    <div class="field">Email Address</div>
    <span class="subscribe">SUBSCRIBE</span>
  </div>
  <div class="footer-name">FERNBROOK PLOTS</div>
</footer>

<div class="legal-bar">
  <span class="copy">Copyright © 2017 FERNBROOK PLOTS. All Rights Reserved.</span>
  <div class="accept"><em>We Accept</em><span class="card"></span><span class="card"></span><span class="card"></span></div>
</div>

</body>
</html>
```